Tarvimoor business cards

Need fresh design for our business cards. Logo must be specific, we are open for everything else.

Contact Information for Business Card

phrase "GMP & JANITORIAL SERVICES" should be used as main point of card

Colors
3176b5
3276b5
85acd3
cedeed
ffffff
0292cd
33a6d7
85cae6
cee9f5

Requirements
Must have
• The logo
Should not have
• crowded designs

```html
<!DOCTYPE html>
<html lang="en">
<head>
<meta charset="utf-8">
<title>Tarvimoor business cards</title>
<link href="https://fonts.googleapis.com/css2?family=Jost:wght@300;400;500&display=swap" rel="stylesheet">
<style>
  :root {
    --backdrop: #1c1f24;
    --brand-blue: #3176b5;
    --sky-blue: #0292cd;
    --mist-blue: #85acd3;
    --pale-blue: #cedeed;
    --ice-blue: #cee9f5;
    --paper: #ffffff;
  }
  * { margin: 0; padding: 0; box-sizing: border-box; }
  html, body { width: 1200px; height: 900px; overflow: hidden; }
  body {
    background: var(--backdrop);
    font-family: "Jost", "Futura", sans-serif;
    display: flex;
    flex-direction: column;
    align-items: center;
    justify-content: center;
    gap: 48px;
  }
  .card {
    width: 660px;
    height: 378px;
    position: relative;
  }
  .card-front { background: var(--brand-blue); }
  .card-back { background: var(--paper); }

  .brand {
    display: flex;
    flex-direction: column;
    align-items: flex-start;
  }
  .brand-name {
    font-weight: 400;
    letter-spacing: 0.14em;
    line-height: 1;
  }
  .brand-tagline {
    font-weight: 500;
    letter-spacing: 0.2em;
    text-transform: uppercase;
    margin-top: 8px;
    align-self: flex-end;
    white-space: nowrap;
  }

  .card-front .brand {
    position: absolute;
    left: 50%;
    top: 50%;
    transform: translate(-50%, -50%);
  }
  .card-front .brand-name { font-size: 52px; color: var(--paper); }
  .card-front .brand-tagline { font-size: 13px; color: var(--ice-blue); }

  .card-back .brand {
    position: absolute;
    left: 44px;
    top: 156px;
  }
  .card-back .brand-name { font-size: 34px; color: var(--brand-blue); }
  .card-back .brand-tagline { font-size: 9px; color: var(--sky-blue); margin-top: 6px; }

  .divider {
    position: absolute;
    left: 362px;
    top: 60px;
    width: 1px;
    height: 250px;
    background: var(--mist-blue);
  }
  .contact {
    position: absolute;
    left: 392px;
    top: 70px;
    color: var(--brand-blue);
    font-weight: 400;
    font-size: 16px;
    line-height: 1.3;
  }
  .contact-name {
    font-size: 18px;
    font-weight: 500;
    letter-spacing: 0.06em;
    text-transform: uppercase;
  }
  .contact-role { color: var(--sky-blue); margin-bottom: 22px; }
  .contact-address { margin-bottom: 20px; }
  .contact-line {
    display: flex;
    align-items: center;
    gap: 12px;
    margin-bottom: 4px;
  }
  .contact-line svg { width: 12px; height: 12px; flex: none; color: var(--sky-blue); }
</style>
</head>
<body>
  <section class="card card-front">
    <div class="brand">
      <span class="brand-name">TARVIMOOR</span>
      <span class="brand-tagline">GMP &amp; Janitorial Services</span>
    </div>
  </section>

  <section class="card card-back">
    <div class="brand">
      <span class="brand-name">TARVIMOOR</span>
      <span class="brand-tagline">GMP &amp; Janitorial Services</span>
    </div>
    <div class="divider"></div>
    <div class="contact">
      <p class="contact-name">Miles Halvorsen</p>
      <p class="contact-role">Director</p>
      <p class="contact-address">1187 Fernbrook Lane<br>Ridgeport, OR 97488</p>
      <p class="contact-line">
        <svg viewBox="0 0 12 12" aria-hidden="true"><path d="M3 1 L5 3.5 L4 5 Q5 7 7 8 L8.5 7 L11 9 L9.5 11 Q4 10.5 1 3 Z" fill="none" stroke="currentColor" stroke-width="1"/></svg>
        (555) 210-4386
      </p>
      <p class="contact-line">
        <svg viewBox="0 0 12 12" aria-hidden="true"><rect x="1" y="2.5" width="10" height="7" fill="none" stroke="currentColor" stroke-width="1"/><path d="M1 2.5 L6 6.5 L11 2.5" fill="none" stroke="currentColor" stroke-width="1"/></svg>
        info@tarvimoor.com
      </p>
      <p class="contact-line">
        <svg viewBox="0 0 12 12" aria-hidden="true"><circle cx="6" cy="6" r="5" fill="none" stroke="currentColor" stroke-width="1"/><ellipse cx="6" cy="6" rx="2.2" ry="5" fill="none" stroke="currentColor" stroke-width="0.8"/><path d="M1 6 H11" stroke="currentColor" stroke-width="0.8"/></svg>
        www.tarvimoor.com
      </p>
    </div>
  </section>
</body>
</html>
```